Business Cards for a Junk Removal Company

Hello,
We are looking to have business cards designed that are simple, bold, easy to read, and right to the point. Please see the attachments for our logo files. We want the card to be yellow on both sides ( Color code Yellow: #FFE01B). The logo text font is (Rockstar Extra Bold) and this is also in the files attached. Please make the text black for the logo. On the back side of the card, you can use white and black for text. Thank you in advance for your hard work!

Front of card-
Harbor Haul Away (logo)
Back of card-
Harbor Haul Away
Donate - Recycle - Dispose
555-271-8093
www.harborhaulaway.example
info@harborhaulaway.example

Industry/Entity Type

Junk removal

Contact Information for Business Card

FRONT OF CARD- Harbor Haul Away (logo) BACK OF CARD- Harbor Haul Away Donate - Recycle - Dispose 555-271-8093 www.harborhaulaway.example info@harborhaulaway.example

Font styles to use
Other font styles liked:
• Rockstar Extra Bold

Colors
FFF300
FFF600
FEFA6F
FFFEC7
FFFEE8

Requirements
Must have
• Must have color code Yellow: #FFE01B for the background of front and back of the card

```html
<!DOCTYPE html>
<html lang="en">
<head>
<meta charset="utf-8">
<title>Harbor Haul Away – Business Cards</title>
<link rel="stylesheet" href="https://fonts.googleapis.com/css2?family=Anton&display=swap">
<style>
  :root {
    --card-yellow: #FFE01B;
    --ink: #0a0a0a;
    --backdrop: #c9c9c9;
  }
  * { margin: 0; padding: 0; box-sizing: border-box; }
  html, body { width: 1200px; height: 800px; overflow: hidden; }
  body {
    background: var(--backdrop);
    font-family: "Anton", "Arial Narrow", sans-serif;
    display: flex;
    align-items: center;
    justify-content: center;
    gap: 30px;
  }
  .card {
    position: relative;
    width: 560px;
    height: 320px;
    background: var(--card-yellow);
    overflow: hidden;
    color: var(--ink);
  }

  /* Contact side */
  .card--contact .brand {
    position: absolute;
    left: 22px;
    top: 0;
    width: 210px;
    height: 100%;
    display: flex;
    flex-direction: column;
    justify-content: center;
    text-transform: uppercase;
    line-height: 0.95;
  }
  .card--contact .brand-line-1 { font-size: 60px; }
  .card--contact .brand-line-2 { font-size: 33px; letter-spacing: 2px; }

  .contact-panel {
    position: absolute;
    left: 250px;
    right: 0;
    top: 38px;
    bottom: 38px;
    display: flex;
    flex-direction: column;
    gap: 6px;
  }
  .contact-row {
    flex: 1;
    display: flex;
    align-items: stretch;
    background: var(--ink);
    color: var(--card-yellow);
  }
  .contact-icon {
    width: 58px;
    display: flex;
    align-items: center;
    justify-content: center;
    border-right: 2px solid #222;
  }
  .contact-icon svg { width: 26px; height: 26px; }
  .contact-text {
    display: flex;
    align-items: center;
    padding-left: 14px;
    font-size: 17px;
    letter-spacing: 0.5px;
    text-transform: uppercase;
    white-space: nowrap;
  }
  .contact-row--phone .contact-text { font-size: 24px; letter-spacing: 1px; }

  /* Front side */
  .card--front {
    display: flex;
    flex-direction: column;
    align-items: center;
    justify-content: center;
    text-transform: uppercase;
  }
  .card--front .brand { text-align: center; line-height: 0.9; }
  .card--front .brand-line-1 { font-size: 112px; letter-spacing: 1px; }
  .card--front .brand-line-2 { font-size: 46px; letter-spacing: 14px; margin-right: -14px; }
  .tagline {
    margin-top: 26px;
    font-size: 24px;
    letter-spacing: 1px;
  }
</style>
</head>
<body>

<section class="card card--contact" aria-label="Contact side">
  <div class="brand">
    <span class="brand-line-1">Harbor</span>
    <span class="brand-line-2">Haul Away</span>
  </div>

  <div class="contact-panel">
    <div class="contact-row contact-row--phone">
      <div class="contact-icon">
        <svg viewBox="0 0 24 24" aria-hidden="true">
          <path fill="#FFE01B" d="M6.6 10.8a15.1 15.1 0 0 0 6.6 6.6l2.2-2.2c.3-.3.7-.4 1-.2 1.1.4 2.3.6 3.6.6.6 0 1 .4 1 1V20c0 .6-.4 1-1 1A17 17 0 0 1 3 4c0-.6.4-1 1-1h3.5c.6 0 1 .4 1 1 0 1.3.2 2.5.6 3.6.1.3 0 .7-.2 1z"/>
        </svg>
      </div>
      <div class="contact-text">555-271-8093</div>
    </div>

    <div class="contact-row">
      <div class="contact-icon">
        <svg viewBox="0 0 24 24" aria-hidden="true">
          <rect x="2" y="5" width="20" height="14" fill="#FFE01B"/>
          <path d="M2 5l10 8 10-8" fill="none" stroke="#0a0a0a" stroke-width="1.6"/>
        </svg>
      </div>
      <div class="contact-text">info@harborhaulaway.example</div>
    </div>

    <div class="contact-row">
      <div class="contact-icon">
        <svg viewBox="0 0 24 24" aria-hidden="true" fill="none" stroke="#FFE01B" stroke-width="1.8">
          <circle cx="12" cy="12" r="9.5"/>
          <ellipse cx="12" cy="12" rx="4.2" ry="9.5"/>
          <path d="M2.5 12h19M4 7h16M4 17h16"/>
        </svg>
      </div>
      <div class="contact-text">www.harborhaulaway.example</div>
    </div>
  </div>
</section>

<section class="card card--front" aria-label="Front side">
  <div class="brand">
    <div class="brand-line-1">Harbor</div>
    <div class="brand-line-2">Haul Away</div>
  </div>
  <p class="tagline">Donate - Recycle - Dispose</p>
</section>

</body>
</html>
```